Redesign of our brintaval.com VPS mini site

We need to a full redesign (modern, fancy and attractive) with a new logo. The site is http://www.brintaval.com/

We are open to any idea / suggestion. Content will not be much more than what is present on the actual web site. We would like to see more filler images inside the page.

Into the attached files I've included all the current web pages
Updates

Project Deadline Extended
Reason: Need more time to make a choice.

Target Market(s)

Internet Hosting

Industry/Entity Type

Internet Service Provider

Logo Text

Quarly BrinTaval

Coding

Coded - Design and coding required

Number of Pages Required

3 page

Font styles to use
Sans Serif

```html
<!DOCTYPE html>
<html lang="en">
<head>
<meta charset="utf-8">
<title>Brintaval – VPS Hosting</title>
<link href="https://fonts.googleapis.com/css2?family=Lato:wght@300;400;700&family=Arimo:wght@400;700&display=swap" rel="stylesheet">
<style>
:root{
  --ink:#2b2b2b;
  --muted:#5a5a5a;
  --page:#f4f4f4;
  --card:#ffffff;
  --header:#161616;
  --footer:#1b1b1b;
  --footer-text:#a9a9a9;
  --gold:#e8a317;
  --green:#7aab1e;
  --btn-dark:#2a2a2a;
  --rule:#dcdcdc;
  --list-text:#555555;
  --bullet:#aaaaaa;
}
*{margin:0;padding:0;box-sizing:border-box}
html,body{width:1200px;height:1200px;overflow:hidden}
body{position:relative;background:var(--page);font-family:"Arimo",Arial,sans-serif;color:var(--ink)}
.abs{position:absolute}

.site-header{left:0;top:0;width:1200px;height:60px;background:var(--header);border-bottom:1px solid #2a2a2a}
.brand{left:259px;top:14px;display:flex;align-items:center;gap:12px;font-family:"Lato",sans-serif}
.brand-mark{width:32px;height:32px;background:var(--gold)}
.brand-name{color:#f2f2f2;font-size:17px;letter-spacing:2px;font-weight:400}
.main-nav{right:238px;top:20px;display:flex;align-items:center;font-size:9px;letter-spacing:1px;color:#cfcfcf}
.main-nav span{padding:0 12px;border-left:1px solid #555}
.main-nav span:first-child{border-left:none}

.hero{left:0;top:60px;width:1200px;height:326px}
.hero-photo{position:absolute;inset:0;background:
  radial-gradient(ellipse 180px 120px at 760px 90px,rgba(200,200,200,.55),transparent 70%),
  radial-gradient(ellipse 300px 200px at 780px 250px,rgba(120,120,120,.35),transparent 70%),
  linear-gradient(90deg,#050607 0%,#0b1119 25%,#10161d 45%,#1e1e1e 70%,#0c0c0c 100%)}
.hero-copy{left:0;width:1236px;top:90px;text-align:center;color:#eee}
.hero-title{font-family:"Lato",sans-serif;font-weight:300;font-size:22px;line-height:28px}
.hero-lead{margin-top:14px;font-size:10px;line-height:14px;color:#bdbdbd}
.slider{left:516px;top:250px;width:186px;height:3px;background:#666}
.slider i{position:absolute;right:0;top:0;width:93px;height:3px;background:var(--gold)}

.product-art{left:288px;top:444px;width:288px;height:150px;background:linear-gradient(180deg,#e9e9e9,#bdbdbd 60%,#f4f4f4)}
.product{left:592px;top:440px;width:380px}
.product h1{font-family:"Lato",sans-serif;font-weight:300;font-size:24px;color:#444}
.product .sub{margin-top:10px;font-family:"Lato",sans-serif;font-size:12.5px;color:#555}
.product p{margin-top:8px;font-size:9px;line-height:14px;color:#333}
.price{margin-top:14px;font-family:"Lato",sans-serif;font-size:22px;color:#333}
.btn-order{display:inline-block;margin-top:16px;width:104px;height:32px;line-height:30px;text-align:center;background:var(--btn-dark);color:#eee;font-family:"Lato",sans-serif;font-size:12px;border-bottom:3px solid #111}

.features{left:258px;top:674px;width:702px;height:224px;background:var(--card);box-shadow:0 8px 10px -8px rgba(0,0,0,.25)}
.feat-group{position:absolute;top:32px;width:294px}
.feat-group h2{font-family:"Lato",sans-serif;font-weight:400;font-size:11px;letter-spacing:.5px;color:#444;padding-bottom:8px;border-bottom:1px solid var(--rule)}
.feat-cols{display:flex;margin-top:12px}
.feat-cols ul{list-style:none;width:144px}
.feat-cols li{font-size:7.5px;line-height:14.2px;color:var(--list-text);padding-left:9px;position:relative}
.feat-cols li::before{content:"»";position:absolute;left:0;color:var(--bullet)}

.cta{left:0;top:934px;width:1200px;text-align:center}
.cta h2{font-family:"Lato",sans-serif;font-weight:300;font-size:23px;color:#444}
.cta .sub{margin-top:6px;font-family:"Lato",sans-serif;font-size:13.5px;color:#555}
.btn-go{display:inline-block;margin-top:18px;width:121px;height:32px;line-height:30px;background:var(--green);color:#fff;font-weight:700;font-size:9.5px;letter-spacing:1px;border-bottom:3px solid #5b8612}
.cta .note{margin-top:14px;font-size:8.5px;color:#333}

.site-footer{left:0;top:1094px;width:1200px;height:106px;background:var(--footer);color:var(--footer-text);font-size:8px}
.foot-brand{left:259px;top:34px;display:flex;align-items:center;gap:10px;font-family:"Lato",sans-serif}
.foot-brand .brand-mark{width:24px;height:18px}
.foot-brand .brand-name{color:#9a9a9a;font-size:14px}
.copyright{left:259px;top:62px;font-size:7px}
.divider{top:30px;width:1px;height:40px;background:#3a3a3a}
.foot-list{top:32px;line-height:14.5px;color:var(--footer-text)}
.social{left:834px;top:36px;display:flex;gap:3px}
.social i{width:14px;height:14px;background:#3a3a3a;display:block}
</style>
</head>
<body>
<header class="abs site-header">
  <div class="abs brand"><div class="brand-mark"></div><div class="brand-name">BRINTAVAL</div></div>
  <nav class="abs main-nav">
    <span><svg width="10" height="9" viewBox="0 0 10 9"><path d="M5 0 0 4.5h1.5V9h2.5V6h2v3h2.5V4.5H10z" fill="#e6e6e6"/></svg></span>
    <span>FAQ</span><span>DDOS</span><span>CONTACT</span>
  </nav>
</header>

<section class="abs hero">
  <div class="hero-photo" role="img" aria-label="Photo of hands holding a tablet with a cloud and server icons floating above it, on a dark data-centre background"></div>
  <div class="abs hero-copy">
    <div class="hero-title">We provide top end, high storage virtual<br>servers at affordable prices.</div>
    <div class="hero-lead">Lorem ipsum dolor sit amet, consectetur adipiscing elit. Ut vel pharetra diam. Aenean<br>convallis nibh facilisis risus convallis, non ornare tellus vehicula.</div>
  </div>
  <div class="abs slider"><i></i></div>
</section>

<div class="abs product-art" role="img" aria-label="Illustration of rack and tower servers with a mascot figure on top"></div>
<section class="abs product">
  <h1>Unmanaged NestVM private server</h1>
  <div class="sub">So, what's the deal? You will get</div>
  <p>We highly recommend to buy also the DDOS protected IP. It's only £ 5.00 more per month and can protect from some of the most common attack to up to 10Gbps and 1 Million packets per second.</p>
  <div class="price">$5.00/m</div>
  <span class="btn-order">ORDER NOW</span>
</section>

<section class="abs features">
  <div class="feat-group" style="left:42px">
    <h2>BRINTAVAL VPS FEATURES</h2>
    <div class="feat-cols">
      <ul><li>4 CPU Cores</li><li>4 GB RAM</li><li>40 GB DISK</li><li>2000 GB Traffic</li><li>Nixora Operating System</li><li>TUN / TAP / PPP / FUSE</li><li>1 IPv4, 4 IPv6</li></ul>
      <ul><li>Shared Gigabit speed</li><li>Sorvia Control Panel</li><li>Location: Milan, Italy</li><li>Test IP 198.51.100.0</li><li>Unmanaged service</li><li>No refund</li></ul>
    </div>
  </div>
  <div class="feat-group" style="left:372px">
    <h2>ONLY FOR GBP £ 5 MONTHLY</h2>
    <div class="feat-cols">
      <ul><li>Cedrix OS 5 32/64 bit</li><li>Cedrix OS 6 32/64 bit</li><li>Dabrin 6 32/64 bit</li><li>Ulvana 10.04 32/64 bit</li><li>Ulvana 11.10 32/64 bit</li><li>Ulvana 12.04 32/64 bit</li><li>Ulvana 12.10 32/64 bit</li></ul>
      <ul><li>Hostelkit - Cedrix OS 5</li><li>Keyturn Nixora Pressly</li><li>Keyturn Nixora forumKit</li></ul>
    </div>
  </div>
</section>

<section class="abs cta">
  <h2>Are you ready to start?</h2>
  <div class="sub">High density, state of the art NestVM containers</div>
  <span class="btn-go">ORDER NOW &nbsp;!</span>
  <div class="note">Not sure where to start? Chat to a support representative now</div>
</section>

<footer class="abs site-footer">
  <div class="abs foot-brand"><div class="brand-mark"></div><div class="brand-name">BRINTAVAL</div></div>
  <div class="abs copyright">© Copyright 2015 | Company Name. All rights reserved</div>
  <div class="abs divider" style="left:469px"></div>
  <div class="abs foot-list" style="left:533px">Write us an Email<br>Live Chat 24 / 7<br>Support: +00 (55) 0100 2020</div>
  <div class="abs foot-list" style="left:701px">Home<br>FAQ<br>DDOS</div>
  <div class="abs divider" style="left:778px"></div>
  <div class="abs social"><i></i><i></i><i></i><i></i><i></i></div>
</footer>
</body>
</html>
```